Dorian Valek Photography Business Card

I am a photographer in Philadelphia, PA. I have a business card that I have designed in Photoshop. This has been an ongoing process for me for far too long. I am 85% pleased with what I have. I need some experts like yourself who has that extra 25% to make this card 110%. I use the dots throughout my website as page/topic breaks. I also use the dots on the mailing side of my direct mail pieces.

Bramble Printworks does my printing.
Their File Specs for a business card:
width - 3.625 inches
Height - 2.124 inches
@ 355 PPI or DPI
CMYK
1/8 inch Bleed/CUT
This is the size of my uploaded file samples

I will have the card printed on a 18 pt card stock - 4 color - 2 sides - with a matte coating

Tech Info: SIDE 01
For name DORIAN VALEK : font choice is FoglihtenNo07 - size 14.4 - VA 150 - Text Height 140% - text width 130% - underlined - color is 30 - 30- 30 or (1e1e1e)
For word PHOTOGRAPHY : font choice is FoglihtenNo07 - size 6.4 - VA 360 - Text Height 200% - text width 270% - underlined - color is 162-162-162 or (a2a2a2)
For DOTS - font choice is FoglihtenNo07 - size 6.73 - VA 180 - Text Height 100% - text width 163% - color is 100-179-204 or (64b3cc) - blue dots / 1-1-1 or (010101) - Black dots
For DORI@DVALEKSTUDIO.EXAMPLE - font choice is Helvetica Neue Light - size 4.55 - VA 121 - Text Height 200% - text width 132% - color is 1-1-1 or (010101)
For 555.418.2736 - font choice is Helvetica Neue Light - size 4.55 - VA 270 - Text Height 180% - text width 189% - color is 1-1-1 or (010101)
For DVALEKSTUDIO.EXAMPLE - font choice is Helvetica Neue Light - size 9.1 - VA 180 - Text Height 150% - text width 130% - color is 133-192-214 or (85c0d6)

Tech Info: SIDE 02
not certain if it is my website address - DVALEKSTUDIO.EXAMPLE - like the sample or
or my Logo with dots DORIAN VALEK PHOTOGRAPHY, WITH UNDERLINEs AND DOTS JUST LIKE FIRST SIDE - MAYBE BIGGER
the name in Helvetica Neue Light - 255 pure white -
Dots are same colors as first side
The background color of choice - at least for now issssss: 84-91-99 or (545b63)

If you think you can make my card really say Wow! Please let me know. Thank you very much!

Target Market(s)

Ad Agencies

Industry/Entity Type

Professional Photography

Contact Information for Business Card

width - 3.625 inches
Height - 2.124 inches
@ 355 PPI or DPI
CMYK
1/8 inch Bleed/CUT

Tech Info: SIDE 01

Tech Info: SIDE 02

Font styles to use
Other font styles liked:
• FoglihtenNo07 and Helvetica Neue Light

Requirements
Must have
• I am a photographer in Philadelphia, PA. I have a business card that I have designed in Photoshop. This has been an ongoing process for me for far too long. I am 85% pleased with what I have. I need some experts like yourself who has that extra 25% to make this card 110%. I use the dots throughout my website as page/topic breaks. I also use the dots on the mailing side of my direct mail pieces.
• Bramble Printworks does my printing.
• Their File Specs for a business card:
• width - 3.625 inches
• Height - 2.124 inches
• @ 355 PPI or DPI
• CMYK
• 1/8 inch Bleed/CUT
• This is the size of my uploaded file samples
• I will have the card printed on a 18 pt card stock - 4 color - 2 sides - with a matte coating
• Tech Info: SIDE 01
• For name DORIAN VALEK : font choice is FoglihtenNo07 - size 14.4 - VA 150 - Text Height 140% - text width 130% - underlined - color is 30 - 30- 30 or (1e1e1e)
• For word PHOTOGRAPHY : font choice is FoglihtenNo07 - size 6.4 - VA 360 - Text Height 200% - text width 270% - underlined - color is 162-162-162 or (a2a2a2)
• For DOTS - font choice is FoglihtenNo07 - size 6.73 - VA 180 - Text Height 100% - text width 163% - color is 100-179-204 or (64b3cc) - blue dots / 1-1-1 or (010101) - Black dots
• For DORI@DVALEKSTUDIO.EXAMPLE - font choice is Helvetica Neue Light - size 4.55 - VA 121 - Text Height 200% - text width 132% - color is 1-1-1 or (010101)
• For 555.418.2736 - font choice is Helvetica Neue Light - size 4.55 - VA 270 - Text Height 180% - text width 189% - color is 1-1-1 or (010101)
• For DVALEKSTUDIO.EXAMPLE - font choice is Helvetica Neue Light - size 9.1 - VA 180 - Text Height 150% - text width 130% - color is 133-192-214 or (85c0d6)
• Tech Info: SIDE 02
• not certain if it is my website address - DVALEKSTUDIO.EXAMPLE - like the sample or
• or my Logo with dots DORIAN VALEK PHOTOGRAPHY, WITH UNDERLINEs AND DOTS JUST LIKE FIRST SIDE - MAYBE BIGGER
• the name in Helvetica Neue Light - 255 pure white -
• Dots are same colors as first side
• The background color of choice - at least for now issssss: 84-91-99 or (545b63)
• If you think you can make my card really say Wow! Please let me know. Thank you very much!
Nice to have
• I could really use some different sizes of the dots as a Vector file?? I use Photoshop for all my designs. Thank You.
Should not have
• all listed above

```html
<!DOCTYPE html>
<html lang="en">
<head>
<meta charset="utf-8">
<title>Dorian Valek Photography — Business Card</title>
<link rel="stylesheet" href="https://fonts.googleapis.com/css2?family=Bodoni+Moda:wght@400;500&family=Roboto:wght@300;400&display=swap">
<style>
  :root {
    --backdrop: #e8e5e0;
    --card-white: #ffffff;
    --card-black: #141414;
    --ink: #1e1e1e;
    --ink-soft: #010101;
    --rule: #6f6f6f;
    --accent: #2aa9c9;
    --dot-blue: #3fb3d1;
    --dot-black: #010101;
    --paper-white: #ffffff;
  }
  * { box-sizing: border-box; margin: 0; padding: 0; }
  html, body {
    width: 1200px;
    height: 800px;
    overflow: hidden;
    background: var(--backdrop);
  }
  .sheet {
    position: relative;
    width: 1200px;
    height: 800px;
    display: flex;
    align-items: center;
    justify-content: center;
    gap: 40px;
  }
  .card {
    position: relative;
    width: 540px;
    height: 309px;
    box-shadow: 0 10px 24px rgba(0,0,0,0.18);
    overflow: hidden;
  }

  /* Website side */
  .card--back {
    background: var(--card-black);
    display: flex;
    align-items: center;
    justify-content: center;
  }
  .site-frame {
    border: 1.5px solid var(--accent);
    padding: 16px 26px;
  }
  .site-frame__url {
    font-family: "Roboto", sans-serif;
    font-weight: 400;
    font-size: 23px;
    letter-spacing: 0.2em;
    color: var(--paper-white);
    white-space: nowrap;
  }

  /* Contact side */
  .card--front { background: var(--card-white); }
  .wordmark {
    position: absolute;
    left: 62px;
    top: 44px;
    width: 420px;
  }
  .wordmark__name {
    font-family: "Bodoni Moda", serif;
    font-weight: 400;
    font-size: 44px;
    line-height: 1;
    letter-spacing: 0.03em;
    color: var(--ink);
    white-space: nowrap;
    text-align: right;
  }
  .wordmark__rule {
    height: 1px;
    background: var(--rule);
    margin-top: 10px;
  }
  .wordmark__trade {
    font-family: "Roboto", sans-serif;
    font-weight: 400;
    font-size: 17px;
    letter-spacing: 0.95em;
    margin-right: -0.95em;
    color: var(--ink);
    text-align: right;
    margin-top: 8px;
    white-space: nowrap;
  }
  .dot-rule {
    position: absolute;
    left: 22px;
    top: 176px;
  }
  .contact {
    font-family: "Roboto", sans-serif;
    font-weight: 400;
    color: var(--ink-soft);
    position: absolute;
    white-space: nowrap;
  }
  .contact--email {
    left: 42px;
    top: 216px;
    font-size: 13px;
    letter-spacing: 0.04em;
  }
  .contact--phone {
    right: 46px;
    top: 250px;
    font-size: 14px;
    font-weight: 300;
    letter-spacing: 0.22em;
  }
</style>
</head>
<body>
  <main class="sheet">
    <section class="card card--back" aria-label="Business card, website side">
      <div class="site-frame">
        <p class="site-frame__url">DVALEKSTUDIO.EXAMPLE</p>
      </div>
    </section>

    <section class="card card--front" aria-label="Business card, contact side">
      <div class="wordmark">
        <h1 class="wordmark__name">DORIAN VALEK</h1>
        <div class="wordmark__rule"></div>
        <p class="wordmark__trade">PHOTOGRAPHY</p>
      </div>

      <svg class="dot-rule" width="496" height="10" viewBox="0 0 496 10" aria-hidden="true">
        <g>
          <circle cx="5" cy="5" r="4" fill="var(--dot-blue)"/>
          <circle cx="26" cy="5" r="4" fill="var(--dot-black)"/>
          <circle cx="47" cy="5" r="4" fill="var(--dot-blue)"/>
          <circle cx="68" cy="5" r="4" fill="var(--dot-black)"/>
          <circle cx="89" cy="5" r="4" fill="var(--dot-blue)"/>
          <circle cx="110" cy="5" r="4" fill="var(--dot-black)"/>
          <circle cx="131" cy="5" r="4" fill="var(--dot-blue)"/>
          <circle cx="152" cy="5" r="4" fill="var(--dot-black)"/>
          <circle cx="173" cy="5" r="4" fill="var(--dot-blue)"/>
          <circle cx="194" cy="5" r="4" fill="var(--dot-black)"/>
          <circle cx="215" cy="5" r="4" fill="var(--dot-blue)"/>
          <circle cx="236" cy="5" r="4" fill="var(--dot-black)"/>
          <circle cx="257" cy="5" r="4" fill="var(--dot-blue)"/>
          <circle cx="278" cy="5" r="4" fill="var(--dot-black)"/>
          <circle cx="299" cy="5" r="4" fill="var(--dot-blue)"/>
          <circle cx="320" cy="5" r="4" fill="var(--dot-black)"/>
          <circle cx="341" cy="5" r="4" fill="var(--dot-blue)"/>
          <circle cx="362" cy="5" r="4" fill="var(--dot-black)"/>
          <circle cx="383" cy="5" r="4" fill="var(--dot-blue)"/>
          <circle cx="404" cy="5" r="4" fill="var(--dot-black)"/>
          <circle cx="425" cy="5" r="4" fill="var(--dot-blue)"/>
          <circle cx="446" cy="5" r="4" fill="var(--dot-black)"/>
          <circle cx="467" cy="5" r="4" fill="var(--dot-blue)"/>
          <circle cx="488" cy="5" r="4" fill="var(--dot-black)"/>
        </g>
      </svg>

      <p class="contact contact--email">DORI@DVALEKSTUDIO.EXAMPLE</p>
      <p class="contact contact--phone">555.418.2736</p>
    </section>
  </main>
</body>
</html>
```